political campaign lawn sign - Governor's Council in Massachuesetts

We are looking for a political lawn sign. We are running a campaign for Governor's Council in Massachusetts. This sign will be on the lawn of homes and businesses so people driving by will see it. It needs to be simple and bold. The last name is long so maybe it could say vote for Marty and then Kolbeck will be big a bold on the next line??
We need it to say:
Vote for Martin Kolbeck
Governor's Council.

Target Market(s)

local residents

Industry/Entity Type

Politcal Campaign

Font styles to use
Sans Serif
Other font styles liked:
• not sure what font but a modern looking one such as Helvetica, Arial, Sans Seri, sharp sans..

Colors
0054AA
0677BA
7BADD7
CADEEF
E8F1F8
00AB8E
00BBA5
67D7C9
C6EFE9
E9F9F6
FFF300
FFF600
FEFA6F
FFFEC7
FFFEE8

Requirements
Must have
• My name written out with a Capital D and R but lower case for every other letter so its Marty Kolbeck
Nice to have
• modern font , the Colors of the lawn sign should have Blue, Yellow and White something bold that will stand out
Should not have
• any maps of Massachusetts

```html
<!DOCTYPE html>
<html lang="en">
<head>
<meta charset="utf-8">
<title>Vote Marty Kolbeck – Governor's Council</title>
<link rel="stylesheet" href="https://fonts.googleapis.com/css2?family=Kaushan+Script&family=Montserrat:wght@700;800;900&display=swap">
<style>
  :root {
    --navy: #001a52;
    --yellow: #ffff00;
    --white: #ffffff;
    --ink: #000000;
    --olive: #7e8c26;
  }
  html, body {
    margin: 0;
    padding: 0;
    width: 1200px;
    height: 903px;
    overflow: hidden;
    background: var(--navy);
  }
  .lawn-sign {
    display: block;
    width: 1200px;
    height: 903px;
    background: var(--navy);
  }
  .rule-white { stroke: var(--white); stroke-width: 4; fill: none; }
  .rule-yellow { stroke: var(--yellow); stroke-width: 4; fill: none; }
  .frame { stroke: var(--white); stroke-width: 8; fill: none; stroke-linejoin: round; }
  .star { fill: var(--olive); }
  .vote-script {
    font-family: "Kaushan Script", cursive;
    font-size: 128px;
    fill: var(--yellow);
    stroke: var(--ink);
    stroke-width: 12;
    stroke-linejoin: round;
    paint-order: stroke fill;
  }
  .first-name {
    font-family: "Montserrat", sans-serif;
    font-weight: 900;
    font-size: 440px;
    fill: var(--white);
    stroke: var(--ink);
    stroke-width: 20;
    stroke-linejoin: miter;
    paint-order: stroke fill;
  }
  .last-name {
    font-family: "Montserrat", sans-serif;
    font-weight: 800;
    font-size: 138px;
    fill: var(--yellow);
  }
  .office {
    font-family: "Montserrat", sans-serif;
    font-weight: 800;
    font-size: 56px;
    fill: var(--yellow);
  }
</style>
</head>
<body>
<svg class="lawn-sign" viewBox="0 0 1200 903" xmlns="http://www.w3.org/2000/svg">
  <rect width="1200" height="903" fill="var(--navy)"/>

  <g class="top-rules">
    <line class="rule-white" x1="0" y1="18" x2="1200" y2="-72"/>
    <line class="rule-yellow" x1="0" y1="40" x2="1200" y2="-50"/>
    <line class="rule-white" x1="0" y1="65" x2="1200" y2="-25"/>
  </g>

  <g class="bottom-rules">
    <line class="rule-white" x1="0" y1="832" x2="269" y2="812"/>
    <line class="rule-white" x1="931" y1="767" x2="1200" y2="746"/>
    <line class="rule-white" x1="0" y1="890" x2="1200" y2="800"/>
    <line class="rule-yellow" x1="108" y1="903" x2="1200" y2="821"/>
    <line class="rule-white" x1="434" y1="903" x2="1200" y2="845"/>
    <line class="rule-yellow" x1="705" y1="903" x2="1200" y2="866"/>
  </g>

  <g class="frame-lines">
    <path class="frame" d="M75 803 V125 H255"/>
    <path class="frame" d="M634 125 H1088 V150"/>
    <line class="frame" x1="1088" y1="383" x2="1088" y2="716"/>
  </g>

  <defs>
    <path id="star" d="M0 -1 L0.2245 -0.309 L0.951 -0.309 L0.363 0.118 L0.588 0.809 L0 0.382 L-0.588 0.809 L-0.363 0.118 L-0.951 -0.309 L-0.2245 -0.309 Z"/>
  </defs>
  <g class="stars">
    <use href="#star" class="star" transform="translate(167 182) scale(25)"/>
    <use href="#star" class="star" transform="translate(720 79) scale(19)"/>
    <use href="#star" class="star" transform="translate(929 44) scale(31)"/>
    <use href="#star" class="star" transform="translate(1115 82) scale(31)"/>
    <use href="#star" class="star" transform="translate(654 173) scale(19)"/>
    <use href="#star" class="star" transform="translate(480 288) scale(19)"/>
    <use href="#star" class="star" transform="translate(1036 705) scale(19)"/>
  </g>

  <g class="headline" transform="rotate(-3 600 450)">
    <text class="vote-script" x="450" y="188" text-anchor="middle">Vote</text>
    <text class="first-name" x="112" y="572" textLength="1020" lengthAdjust="spacingAndGlyphs">MARTY</text>
    <text class="last-name" x="125" y="745" textLength="890" lengthAdjust="spacingAndGlyphs">KOLBECK</text>
  </g>

  <text class="office" transform="rotate(-4 600 800)" x="290" y="832" textLength="620" lengthAdjust="spacingAndGlyphs">GOVERNOR'S COUNCIL</text>
</svg>
</body>
</html>
```